Tri-Fold Brochure for Breezy Step Studio
VIVID STEPWORKS
Thank you all for your designs. This is going to be a very tough decision. Such brilliance and creativity! Will choose a winner shortly. Thanks again!
Draft #17
Outside Left, Center, Right: Would it be possible to make the whole side more fluid and continuous like the inside and not broken into panels?
Outside Right: Can you use the image you used in Outside Center for the front cover to give it an instant impact? If you do this, please use another image for Outside Center.
Colin
Draft #21
Great submission. Way to rally!
Outside Right: We need an image that gives more impact for the front cover. Something like what you used for Inside Left. Perhaps use that and another image for Inside Left.
Draft #26
This looks great. I think the chatterloop logo looks good. Just a few more edits with the choice of images used. All of them looks too similar.
Outside Left: Could you use this couple or similar image here? 237519804
Inside Left: Can you use another image like this beautiful solo dancer in red dress here? 864203571
Thanks!
Draft #13
Outside Center: I think you missed the red color change in the word "phone:". Can you also concatenate the word "e mail" to "email" (remove space).
Does the chatterloop logo need to be on the back? I took it out because something about it didn't look right with the rest of the content.
Draft #12, Thank you for the quick edits! Just a few more if you don't mind.
Inside Left: Can you make the font in the dance styles bigger? Not sure why I like things bigger but I just want the dance styles to stand out and hits you in the face.
Inside Center: The numbering list starts with "Visit our website..." and step 4 should be separated into two steps. With these correction, we should have a total of 5 steps still.
Outside Left: Can you add a Welcome title and move the Register Online to Inside Right or somewhere between Inside Center and Inside Right?
Outside Center: Not sure how I feel on the look and feel of the "find us on chatterloop" and the web address. For some reason, it seems out of place. Any way to make it a bit more integrated?
Draft #4
For all the section titles, can you use a more modern, blockier font that very easy to read? Also, can you add the website address in the outside center?
All,
I have failed to mention in the word document to include the website address in the outside center. Please add it right after the Address. I have uploaded another version of the document with this detail. Sorry about that. Also, please use an appropriate chatterloop image for Find Us On chatterloop. Thanks!
All I can say is WOW, WOW, WOW! Such great creativity and ideas! Thank you all for your submissions.
Draft #11
Inside Left: Can you highlight or give more weight to the whole section of the Dance Styles We Offer. The weight of the font looks too light and we would like to emphasize our dance offerings.
Inside Center: Is it possible to number list the top part after "Here's how to get started"? Also, can we bullet point the "Things to know" list? It doesn't have to be a bullet, it can be any image.
Outside Center: Can you include our website address?
In general, can you make the section titles much bigger (Dance Styles We Offer, Getting Started, Things to Know)
Draft #8
Love it. For all the red color you used, it seems very burgundy and a bit darker than the red in our logo. Can you make it brighter to march our logo color?
If possible can you add our website address in the outside center under For More Info section?
Hi draft #2. Thank you for your design. I was away on travel so apologies for not providing feedback sooner.
Great first draft. I have attached a word document with all the brochure wording. Please follow this document instead of the description in the brief.
Please use a consistent font all around.
As for the images. I love the front cover image you used that I provided. For the other images from pixelvaultimages, I would like to use couples in more normal clothing so it's more approachable to the general public.
Here are some of the images I really like from pixelvaultimages and hopefully these can work fluidly in your design.
864203571 (Solo dancer that just looks cool)
Thank you so much!

```html
<!DOCTYPE html>
<html lang="en">
<head>
<meta charset="utf-8">
<title>Vivid Stepworks – Tri-Fold Brochure</title>
<link href="https://fonts.googleapis.com/css2?family=Oswald:wght@500;700&family=Open+Sans:wght@400;600;700&display=swap" rel="stylesheet">
<style>
  :root {
    --red: #e01b22;
    --red-deep: #8e0d12;
    --black: #111111;
    --ink: #1c1c1c;
    --white: #ffffff;
    --paper: #f4f4f4;
    --grey: #6b6b6b;
    --backdrop: #e6e6e6;
  }
  * { box-sizing: border-box; margin: 0; padding: 0; }
  html, body { width: 1200px; height: 902px; overflow: hidden; }
  body {
    background: var(--backdrop);
    font-family: "Open Sans", Arial, sans-serif;
    position: relative;
  }
  .panel {
    position: absolute;
    top: 208px;
    width: 210px;
    height: 486px;
    overflow: hidden;
    box-shadow: 0 2px 10px rgba(0,0,0,0.18);
  }
  .section-title {
    font-family: "Oswald", Arial, sans-serif;
    font-weight: 700;
    text-transform: uppercase;
    line-height: 0.95;
  }
  .photo { position: absolute; }
  .shape { position: absolute; left: 0; top: 0; }

  /* Inside spread */
  .inside-spread { position: absolute; left: 50px; top: 208px; width: 630px; height: 486px; }
  .about { left: 50px; background: var(--black); color: var(--white); }
  .about .section-title { position: absolute; left: 14px; top: 16px; font-size: 30px; text-transform: none; font-weight: 500; }
  .about .body-copy { position: absolute; left: 14px; top: 60px; width: 182px; font-size: 7.6px; line-height: 1.5; color: #dddddd; }
  .about .photo {
    left: 0; top: 210px; width: 210px; height: 276px;
    background: radial-gradient(ellipse at 45% 55%, #b3161d 0%, #5a0c10 35%, #1a1a1a 70%);
  }

  .styles { left: 260px; background: var(--white); }
  .styles .section-title.heading { position: absolute; left: 14px; top: 14px; font-size: 22px; color: var(--white); width: 150px; }
  .dance-list { position: absolute; left: 86px; top: 74px; list-style: none; }
  .dance-list li {
    font-family: "Oswald", Arial, sans-serif;
    font-weight: 700;
    font-size: 24px;
    line-height: 1;
    text-transform: uppercase;
    color: var(--ink);
  }
  .dance-list .accent { color: var(--red); }
  .styles .photo {
    left: 20px; top: 190px; width: 170px; height: 296px;
    background: radial-gradient(ellipse at 50% 55%, var(--red) 0%, var(--red-deep) 40%, rgba(255,255,255,0) 72%);
  }

  .started { left: 470px; background: var(--white); color: var(--ink); }
  .started .section-title.heading { position: absolute; left: 14px; top: 14px; font-size: 30px; width: 180px; }
  .started .intro { position: absolute; left: 14px; top: 84px; font-size: 8px; font-weight: 700; }
  .steps { position: absolute; left: 26px; top: 98px; width: 172px; font-size: 7.6px; line-height: 1.55; }
  .simple { position: absolute; left: 14px; top: 170px; font-size: 9px; font-weight: 700; }
  .started .section-title.know { position: absolute; left: 14px; top: 188px; font-size: 18px; color: var(--red); text-transform: none; }
  .notes { position: absolute; left: 14px; top: 214px; list-style: none; font-size: 7.6px; line-height: 1.7; }
  .notes li::before { content: "\25B6"; color: var(--red); font-size: 6px; margin-right: 5px; }
  .started .photo {
    left: 0; top: 290px; width: 210px; height: 196px;
    background: radial-gradient(ellipse at 55% 55%, #9a1a1e 0%, #c8c8c8 45%, var(--white) 75%);
  }

  /* Outside panels */
  .welcome { left: 710px; background: var(--black); color: var(--white); }
  .welcome .section-title { position: absolute; left: 16px; top: 20px; font-size: 34px; text-transform: none; font-weight: 500; }
  .welcome .body-copy { position: absolute; left: 16px; top: 72px; width: 178px; font-size: 8px; line-height: 1.55; }
  .register {
    position: absolute; left: 45px; top: 200px; width: 120px; height: 120px;
    border-radius: 50%; background: var(--white); color: var(--ink);
    display: flex; align-items: center; justify-content: center; text-align: center;
    font-family: "Oswald", Arial, sans-serif; font-weight: 700; font-size: 19px; line-height: 1; text-transform: uppercase;
  }
  .welcome .closing { position: absolute; left: 16px; top: 350px; width: 178px; font-size: 8px; line-height: 1.55; color: #cccccc; }

  .cover { left: 940px; background: var(--black); color: var(--white); }
  .brand { position: absolute; left: 0; top: 34px; width: 210px; display: flex; align-items: center; justify-content: center; gap: 8px; }
  .brand-dot { width: 16px; height: 16px; border-radius: 50%; background: var(--red); }
  .brand-name { font-family: "Oswald", Arial, sans-serif; font-weight: 700; font-size: 20px; color: var(--white); letter-spacing: 0.5px; }
  .cover .photo {
    left: 0; top: 90px; width: 210px; height: 330px;
    background: radial-gradient(ellipse at 45% 50%, #c0161d 0%, #5c0b0f 38%, var(--black) 72%);
  }
  .web { position: absolute; left: 0; bottom: 14px; width: 210px; text-align: center; font-size: 8px; letter-spacing: 1px; color: #bbbbbb; }
</style>
</head>
<body>

  <!-- Inside: About -->
  <section class="panel about">
    <h2 class="section-title">About Us</h2>
    <p class="body-copy">Vivid Stepworks is a friendly social dance studio where beginners and seasoned dancers learn together. Our certified instructors teach ballroom, Latin and street styles in a relaxed setting. Whether you want to get fit, meet new people or prepare for a special day, we will help you move with confidence and joy.</p>
    <div class="photo" role="img" aria-label="Photo of a couple dancing together"></div>
    <svg class="shape" width="210" height="486" viewBox="0 0 210 486" aria-hidden="true">
      <polygon points="150,486 210,380 210,486" fill="var(--paper)"/>
    </svg>
  </section>

  <!-- Inside: Dance styles -->
  <section class="panel styles">
    <svg class="shape" width="210" height="486" viewBox="0 0 210 486" aria-hidden="true">
      <polygon points="0,0 210,0 210,20 0,200" fill="var(--black)"/>
    </svg>
    <h2 class="section-title heading">Dance Styles We Offer</h2>
    <ul class="dance-list">
      <li class="accent">Ballroom</li>
      <li>Latin</li>
      <li>Salsa</li>
      <li>Swing</li>
      <li>Tango</li>
      <li class="accent">And More</li>
    </ul>
    <div class="photo" role="img" aria-label="Photo of a solo dancer in a red dress"></div>
  </section>

  <!-- Inside: Getting started -->
  <section class="panel started">
    <h2 class="section-title heading">Getting Started</h2>
    <p class="intro">Here's how to get started:</p>
    <ol class="steps">
      <li>Visit our website and browse classes.</li>
      <li>Pick a class that suits your level.</li>
      <li>Register online or call the studio.</li>
      <li>Choose your start date.</li>
      <li>Show up and start dancing!</li>
    </ol>
    <p class="simple">We told you it was simple!</p>
    <h3 class="section-title know">Things to know:</h3>
    <ul class="notes">
      <li>Wear comfortable shoes.</li>
      <li>No partner needed.</li>
      <li>Arrive ten minutes early.</li>
      <li>First class is free.</li>
    </ul>
    <div class="photo" role="img" aria-label="Photo of a couple in casual clothes dancing"></div>
  </section>

  <!-- Outside: Welcome -->
  <section class="panel welcome">
    <svg class="shape" width="210" height="486" viewBox="0 0 210 486" aria-hidden="true">
      <polygon points="0,0 210,0 210,230 0,290" fill="var(--red)"/>
    </svg>
    <h2 class="section-title">Welcome</h2>
    <p class="body-copy">Welcome to Vivid Stepworks, a dance studio for everyone. Join our group classes or book private lessons and discover how fun learning to dance can be.</p>
    <div class="register">Register<br>Online</div>
    <p class="closing">Sign up in minutes on our website and reserve your spot in the next class series.</p>
  </section>

  <!-- Outside: Front cover -->
  <section class="panel cover">
    <div class="brand">
      <span class="brand-dot"></span>
      <span class="brand-name">VIVID STEPWORKS</span>
    </div>
    <div class="photo" role="img" aria-label="Photo of a dancing couple lit in red"></div>
    <svg class="shape" width="210" height="486" viewBox="0 0 210 486" aria-hidden="true">
      <polygon points="0,400 210,340 210,420 0,470" fill="var(--red)"/>
    </svg>
    <p class="web">www.vividstepworks.com</p>
  </section>

</body>
</html>
```